Company or website name
- www.brelmontpath.com
- Links to the website
- Owner of Brelmontpath. We serve real estate brokers, managers & sales associates with consulting, coaching and training solutions. My site is being redesigned to be more focused on target audience.
- Other Facts

```html
<!DOCTYPE html>
<html lang="en">
<head>
<meta charset="utf-8">
<title>Core Habits of Steady Closers – Brochure Spread</title>
<link rel="stylesheet" href="https://fonts.googleapis.com/css2?family=Cinzel:wght@400;500&family=Arimo&display=swap">
<style>
  :root{
    --backdrop:#aeaa8c;
    --blue-top:#0079c2;
    --blue-mid:#0a5a9c;
    --blue-bottom:#0c4a86;
    --map-tint:#8fb0cf;
    --sun-yellow:#f8d31c;
    --sun-orange:#f38a22;
    --deep-orange:#ef5f22;
    --leaf-green:#9cc63a;
    --cream:#fff6df;
    --white:#ffffff;
    --frame:#111111;
  }
  *{margin:0;padding:0;box-sizing:border-box}
  html,body{width:1200px;height:924px;overflow:hidden;background:var(--backdrop)}
  .canvas{position:relative;width:1200px;height:924px}
  .back-cover{
    position:absolute;left:51px;top:73px;width:549px;height:778px;
    background:linear-gradient(180deg,var(--blue-top) 0%,var(--blue-mid) 45%,var(--blue-bottom) 100%);
  }
  .world-map{
    position:absolute;left:119px;top:328px;width:300px;height:151px;
    background:radial-gradient(ellipse at 50% 50%,var(--map-tint) 0%,rgba(143,176,207,.55) 60%,rgba(143,176,207,0) 75%);
    opacity:.85;
  }
  .testimonial-photo{
    position:absolute;left:18px;top:611px;width:161px;height:154px;
    border:5px solid var(--frame);
    background:linear-gradient(180deg,#a9c7e3 0%,#b89a86 55%,#3f6a4a 100%);
  }
  .testimonial-quote{
    position:absolute;left:187px;top:613px;width:362px;
    font-family:"Arimo",Arial,sans-serif;font-size:21px;line-height:30px;color:var(--white);
  }
  .testimonial-quote .line{display:block;white-space:nowrap}
  .testimonial-quote .indent{padding-left:8px}
  .testimonial-author{
    position:absolute;left:393px;top:716px;
    font-family:"Arimo",Arial,sans-serif;font-size:21px;line-height:31px;color:var(--white);
  }
  .front-cover{position:absolute;left:600px;top:73px;width:555px;height:778px;overflow:hidden}
  .front-cover svg{position:absolute;left:0;top:0}
  .title-emblem{
    position:absolute;left:22px;top:15px;width:137px;height:75px;
    background:radial-gradient(ellipse at 50% 50%,rgba(255,255,255,.9) 0%,rgba(255,255,255,.5) 55%,rgba(255,255,255,0) 72%);
  }
  .cover-photo{position:absolute;left:0;top:128px;width:555px;height:440px}
  .cover-title{
    position:absolute;left:176px;top:14px;
    font-family:"Cinzel",Georgia,serif;font-weight:500;font-size:40px;line-height:49px;
    color:var(--white);letter-spacing:.5px;white-space:nowrap;
  }
  .cover-subtitle{
    position:absolute;left:0;top:673px;width:555px;text-align:center;padding-right:10px;
    font-family:"Cinzel",Georgia,serif;font-size:25px;line-height:34px;color:var(--cream);
    letter-spacing:.6px;white-space:nowrap;
  }
  .cover-url{
    position:absolute;left:0;top:743px;width:555px;text-align:center;padding-right:10px;
    font-family:"Arimo",Arial,sans-serif;font-size:20px;color:var(--cream);
  }
</style>
</head>
<body>
<main class="canvas">
  <section class="back-cover">
    <div class="world-map" role="img" aria-label="Pale world map silhouette"></div>
    <div class="testimonial-photo" role="img" aria-label="Portrait photo of the client giving the testimonial"></div>
    <p class="testimonial-quote">
      <span class="line">"This has helped my business.</span>
      <span class="line indent">There is nothing comparable for</span>
      <span class="line indent">a real estate broker.&nbsp; Thanks!"</span>
    </p>
    <p class="testimonial-author">Dale R.<br>Meridian, MS</p>
  </section>

  <section class="front-cover">
    <svg width="555" height="778" viewBox="0 0 555 778" aria-hidden="true">
      <defs>
        <linearGradient id="sunGradient" x1="0" y1="0" x2="1" y2="0">
          <stop offset="0" stop-color="var(--sun-yellow)"/>
          <stop offset=".55" stop-color="var(--sun-orange)"/>
          <stop offset="1" stop-color="var(--deep-orange)"/>
        </linearGradient>
        <linearGradient id="photoTone" x1="0" y1="0" x2="1" y2="1">
          <stop offset="0" stop-color="#6f8a4e"/>
          <stop offset=".45" stop-color="#3a3a44"/>
          <stop offset="1" stop-color="#9a8f86"/>
        </linearGradient>
        <linearGradient id="leafGradient" x1="0" y1="0" x2="1" y2="0">
          <stop offset="0" stop-color="#6fa82c"/>
          <stop offset="1" stop-color="var(--leaf-green)"/>
        </linearGradient>
      </defs>
      <rect class="cover-ground" width="555" height="778" fill="url(#sunGradient)"/>
      <path class="top-swoosh" d="M0,118 C150,175 360,170 555,115 L555,148 L0,148 Z" fill="var(--white)"/>
      <path class="bottom-swoosh-white" d="M0,530 C170,640 380,660 555,600 L555,640 C380,690 170,670 0,575 Z" fill="var(--white)"/>
      <path class="bottom-swoosh-green" d="M0,520 C160,620 380,640 555,580 L555,615 C380,668 170,650 0,560 Z" fill="url(#leafGradient)"/>
      <path class="cover-photo-shape" d="M0,128 C150,183 360,178 555,125 L555,520 C380,600 160,590 0,505 Z" fill="url(#photoTone)"/>
    </svg>
    <div class="cover-photo" role="img" aria-label="Photo of a real estate agent in a suit talking with a client at an office desk"></div>
    <div class="title-emblem" role="img" aria-label="Small white world map emblem"></div>
    <h1 class="cover-title">Core Habits of<br>Steady Closers</h1>
    <p class="cover-subtitle">A Property Agent's Handbook<br>for a Thriving Practice</p>
    <p class="cover-url">www.brelmontpath.com</p>
  </section>
</main>
</body>
</html>
```